A4 Flyer

Bright Path Learning is starting a course in regional Victoria. We are currently advertising (See attached file A34984) in local papers but need to create a one page flyer to distribute to Aged Care facilities in the area. The A4 flyer will be inserted into a folder pack with more detailed information on Bright Path Learning. Important to use images and logoes attached

Target Market(s)

Flyer to be distributed to Aged Care facility staff and owners

Industry/Entity Type

Advertising

Font styles to use
Sans Serif

Colors
f37123
ec1f27

Requirements
Must have
• BPL Logo
Some image

```html
<!DOCTYPE html>
<html lang="en">
<head>
<meta charset="utf-8">
<title>Bright Path Learning – A4 Flyer</title>
<link href="https://fonts.googleapis.com/css2?family=Montserrat:wght@700;800&family=Questrial&family=Roboto+Condensed:wght@400&display=swap" rel="stylesheet">
<style>
  :root {
    --orange: #f37123;
    --red: #ec1f27;
    --orange-deep: #ee5424;
    --ink: #444444;
    --grey: #555555;
    --white: #ffffff;
    --stage: #6d6d6d;
  }
  * { box-sizing: border-box; margin: 0; padding: 0; }
  html, body { width: 1200px; height: 1000px; overflow: hidden; }
  body {
    background: var(--stage);
    font-family: "Questrial", "Century Gothic", sans-serif;
    position: relative;
  }
  .flyer {
    position: absolute;
    left: 275px;
    top: 40px;
    width: 650px;
    height: 920px;
    background: var(--white);
    overflow: hidden;
    box-shadow: 0 4px 14px rgba(0,0,0,0.35);
  }
  .flyer-bands { position: absolute; inset: 0; }
  .abs { position: absolute; }

  .headline {
    left: 0; width: 650px; top: 20px; text-align: center;
    font-family: "Montserrat", sans-serif; font-weight: 800;
    font-size: 35px; letter-spacing: 1px; color: var(--white);
  }
  .headline-sub {
    left: 0; width: 650px; top: 78px; text-align: center;
    font-size: 19px; color: var(--white);
  }
  .qualification {
    right: 45px; top: 172px; text-align: right;
    font-family: "Roboto Condensed", sans-serif;
    font-size: 20px; line-height: 33px; color: var(--orange-deep);
  }
  .funding {
    left: 334px; top: 256px;
    font-size: 24px; line-height: 29px; color: var(--ink);
  }
  .funding .price {
    font-family: "Montserrat", sans-serif; font-weight: 800;
    font-size: 36px; color: var(--orange-deep);
  }
  .photo-main {
    left: 0; top: 180px; width: 330px; height: 420px;
    background: linear-gradient(90deg, #4a4442 0%, #6a605c 45%, #c9c4c2 80%, rgba(255,255,255,0) 100%);
  }
  .photo-small {
    border: 2px solid var(--orange);
    background: linear-gradient(160deg, #d8d4d0 0%, #b9b2ad 55%, #8c8480 100%);
  }
  .photo-lecturer { left: 276px; top: 432px; width: 157px; height: 182px; }
  .photo-anatomy  { left: 448px; top: 408px; width: 158px; height: 183px;
    background: linear-gradient(160deg, #e4e2e0 0%, #c7b8b0 50%, #a15e52 100%); }

  .enrol {
    left: 85px; top: 662px;
    font-size: 23px; line-height: 30px; color: var(--white);
  }
  .enrol-row { display: flex; }
  .enrol-label { width: 200px; text-align: right; padding-right: 14px; }

  .brand {
    left: 54px; top: 782px; display: flex; align-items: center; gap: 12px;
  }
  .brand-mark { width: 40px; height: 40px; border-radius: 50%; background: var(--orange); }
  .brand-name {
    font-size: 24px; line-height: 26px; color: var(--grey); width: 150px;
  }
  .brand-divider {
    left: 282px; top: 762px; width: 2px; height: 80px; background: var(--orange);
  }
  .services {
    left: 296px; top: 764px; width: 340px;
    font-size: 17px; line-height: 25.5px; color: var(--ink);
    list-style: none; display: flex; flex-wrap: wrap; column-gap: 8px;
  }
  .services li { display: flex; align-items: center; gap: 4px; white-space: nowrap; }
  .services li::before {
    content: ""; width: 11px; height: 11px; border-radius: 50%;
    background: var(--orange-deep); flex: none;
  }
  .services .full-row { width: 100%; }
  .footnote {
    left: 0; width: 650px; top: 880px; text-align: center;
    font-size: 15.5px; color: var(--orange-deep);
  }
</style>
</head>
<body>
  <main class="flyer">
    <svg class="flyer-bands" width="650" height="920" viewBox="0 0 650 920" aria-hidden="true">
      <defs>
        <linearGradient id="band-top" x1="0" y1="0" x2="1" y2="0">
          <stop offset="0" stop-color="#f37123"/>
          <stop offset="1" stop-color="#ee5424"/>
        </linearGradient>
        <linearGradient id="band-bottom" x1="0" y1="0" x2="1" y2="0">
          <stop offset="0" stop-color="#f37123"/>
          <stop offset="1" stop-color="#ee5424"/>
        </linearGradient>
      </defs>
      <path d="M0,0 H650 V132 Q380,118 0,168 Z" fill="url(#band-top)"/>
      <path d="M0,174 Q380,124 650,138" fill="none" stroke="#ec1f27" stroke-width="2.5"/>
      <path d="M0,586 Q330,610 650,638 V744 H0 Z" fill="url(#band-bottom)"/>
      <path d="M0,580 Q330,604 650,632" fill="none" stroke="#ec1f27" stroke-width="2"/>
    </svg>

    <div class="abs photo-main" role="img" aria-label="Photo of a smiling student seated at a desk in a classroom"></div>

    <h1 class="abs headline">UNIQUE OPPORTUNITY!</h1>
    <p class="abs headline-sub">Fast Track Course - Start July 2014</p>

    <p class="abs qualification">DOUBLE QUALIFICATION - CERT III IN AGED CARE<br>WITH HOME AND COMMUNITY CARE</p>

    <p class="abs funding">Government Funding for<br>Eligible Etudents!<br>Fees from <span class="price">$117</span></p>

    <div class="abs photo-small photo-lecturer" role="img" aria-label="Photo of a trainer seated at a desk reading notes"></div>
    <div class="abs photo-small photo-anatomy" role="img" aria-label="Photo of a trainer working with an anatomy model"></div>

    <div class="abs enrol">
      <div class="enrol-row"><span class="enrol-label">TO ENROL VISIT:</span><span>brightpathlearning.com.au</span></div>
      <div class="enrol-row"><span class="enrol-label">CALL:</span><span>9555 0142</span></div>
    </div>

    <div class="abs brand">
      <span class="brand-mark"></span>
      <span class="brand-name">Bright Path Learning</span>
    </div>
    <div class="abs brand-divider"></div>
    <ul class="abs services">
      <li>Pathology</li>
      <li>Aged Care</li>
      <li>First Aid</li>
      <li>CPR</li>
      <li>Anaphylaxis</li>
      <li>Health Services</li>
      <li class="full-row">Home &amp; Community Care</li>
      <li class="full-row">Medications for PCA’s</li>
    </ul>

    <p class="abs footnote">This training is delivered with VIC and Comm Govt Funding to eligible students</p>
  </main>
</body>
</html>
```